Phuket Thailand - Rental Villa Website

I have a villa for rent in Thailand and require a website - i need to demo pictures/walk through video, local attractions, villa facilities description plus seaonal rates and online booking.

Industry/Entity Type

Rental

Coding

Coded - Design and coding required

```html
<!DOCTYPE html>
<html lang="en">
<head>
<meta charset="utf-8">
<title>Sandbar Villa – Rental Villa</title>
<link rel="stylesheet" href="https://fonts.googleapis.com/css2?family=Oswald:wght@300;400;500&family=Open+Sans:wght@400;600&display=swap">
<style>
:root{
  --blue:#1a8fd6;
  --blue-deep:#0f74c4;
  --ink:#222;
  --grey:#666;
  --line:#d8d8d8;
  --green-head:#0d9b1c;
  --green-dark:#1c6e16;
  --white:#fff;
  --sky:#3fa9e6;
}
*{box-sizing:border-box;margin:0;padding:0}
html,body{width:688px;height:1200px;overflow:hidden;background:#fff}
body{position:relative;font-family:'Open Sans',sans-serif;color:var(--ink)}
.abs{position:absolute}

/* hero */
.hero-photo{left:0;top:0;width:688px;height:400px;
  background:linear-gradient(180deg,#1d5fb8 0%,#5aa0e0 20%,#2f8fb0 32%,#3fb3c4 48%,#8fd0c9 60%,#e6d0a2 74%,#f0dcb3 86%,#fff 100%)}
.hero-photo::after{content:"";position:absolute;right:0;top:30px;width:330px;height:170px;
  background:linear-gradient(200deg,#3f6b2a,#6e8a3d 60%,transparent);opacity:.7;border-radius:60% 0 0 40%}
.bubble{border-radius:50%;background:rgba(255,255,255,.55);border:2px solid #8fcbea;
  box-shadow:0 0 0 3px rgba(255,255,255,.35);display:flex;flex-direction:column;align-items:center;justify-content:center}
.nav-bubble{width:88px;height:88px;font-size:14.5px;color:#444;gap:2px}
.nav-bubble svg{width:28px;height:28px}
.nav-bubble.is-active{color:var(--blue)}
.brand-bubble{left:226px;top:18px;width:236px;height:236px;padding:0 24px;text-align:center}
.brand-name{font-family:'Oswald',sans-serif;font-weight:500;font-size:28px;color:#e39a12;letter-spacing:1px;line-height:1;margin-top:6px}
.brand-rule{width:144px;height:2px;background:#222;margin:18px 0 12px}
.brand-tag{font-family:'Oswald',sans-serif;font-weight:300;font-size:13.5px;line-height:21px;color:#222;text-transform:uppercase}

/* intro columns */
.section-title{font-family:'Oswald',sans-serif;font-size:19px;display:flex;align-items:center;gap:8px;color:#333}
.section-title .accent{color:var(--blue)}
.title-icon{width:26px;height:26px;border-radius:50%;border:1.5px solid #333;display:flex;align-items:center;justify-content:center}
.title-icon svg{width:13px;height:13px}
.welcome-copy p{font-size:9.2px;line-height:13.2px;color:var(--grey);letter-spacing:.2px;margin-bottom:12px;text-align:justify}
.col-divider{left:337px;top:392px;width:1px;height:220px;background:var(--line)}
.facility{left:362px;width:272px;height:72px;border-bottom:2px solid var(--line)}
.facility-photo{position:absolute;left:4px;top:2px;width:56px;height:56px;border-radius:50%;border:2px solid #8fcbea}
.facility h3{position:absolute;left:74px;top:2px;font-family:'Oswald',sans-serif;font-weight:400;font-size:14px;color:#222}
.facility p{position:absolute;left:67px;top:24px;width:205px;font-size:9px;line-height:13.5px;color:var(--grey);letter-spacing:.3px}
.facility a{position:absolute;right:2px;top:51px;font-family:'Oswald',sans-serif;font-size:9px;color:var(--blue)}

/* attractions */
.attractions{left:0;top:656px;width:688px;height:238px;
  background:linear-gradient(180deg,#1c7fd0 0%,#2a95da 50%,#3aa6d9 100%)}
.band-title{font-family:'Oswald',sans-serif;font-size:20px;color:#fff;display:flex;align-items:center;gap:8px}
.band-title .dark{color:#0a1f3a}
.band-title-icon{width:27px;height:27px;border-radius:50%;border:1.5px solid #fff;display:flex;align-items:center;justify-content:center}
.band-title-icon svg{width:14px;height:14px}
.card{top:717px;width:141px;height:149px;background:#fff;box-shadow:0 1px 3px rgba(0,0,0,.3);padding:3px}
.card-photo{width:135px;height:102px}
.card-label{text-align:center;font-size:13.5px;color:var(--blue);margin-top:12px}

/* rates */
.rates{left:0;top:894px;width:688px;height:222px;
  background:linear-gradient(180deg,#2f8a22 0%,#237a1c 45%,#2b7f3a 80%,#4d9a7a 100%)}
.rates-title{left:0;width:688px;top:930px;text-align:center;font-family:'Oswald',sans-serif;font-size:19px;color:#fff}
.rates-title .dark{color:#0c2a0a}
.rates-rule{top:944px;height:1px;background:rgba(255,255,255,.8);width:58px}
.rate-table{left:44px;top:962px;width:599px;border-collapse:collapse;color:#fff}
.rate-table th,.rate-table td{border:1px solid rgba(255,255,255,.85);font-weight:400;text-align:center}
.rate-table th{background:var(--green-head);font-size:14.5px;height:28px}
.rate-table td{font-size:12px;height:27px}
.rate-table th:first-child,.rate-table td:first-child{text-align:left;padding-left:9px}
.book-btn{left:311px;top:1084px;width:65px;height:20px;background:#1189d9;color:#fff;font-family:'Oswald',sans-serif;font-size:12.5px;display:flex;align-items:center;justify-content:center}

/* footer */
.footer-nav{left:0;top:1116px;width:688px;height:28px;background:linear-gradient(180deg,#39c3e6,#8fe0ef);
  display:flex;justify-content:center;align-items:center;gap:0;font-size:9.5px}
.footer-nav span{margin:0 13px;color:#222}
.footer-nav .is-active{color:var(--blue)}
.footer-sand{left:0;top:1144px;width:688px;height:56px;background:linear-gradient(180deg,#efe6d6,#e8dcc4)}
.copyright{left:0;width:688px;top:1169px;text-align:center;font-size:9.2px;color:#222}
.copyright b{color:var(--blue);font-weight:600}
</style>
</head>
<body>

<!-- hero -->
<div class="abs hero-photo" role="img" aria-label="Tropical beach with turquoise sea, green hills and golden sand"></div>

<div class="abs bubble brand-bubble">
  <div class="brand-name">SANDBAR VILLA</div>
  <div class="brand-rule"></div>
  <div class="brand-tag">Lorem ipsum is simply dummy text of the printing and typesetting industry.</div>
</div>

<div class="abs bubble nav-bubble is-active" style="left:106px;top:110px">
  <svg viewBox="0 0 24 24" fill="#222"><path d="M12 3 2 12h3v8h5v-6h4v6h5v-8h3z"/></svg>Home</div>
<div class="abs bubble nav-bubble" style="left:140px;top:210px">
  <svg viewBox="0 0 24 24" fill="#222"><path d="M3 17.2V21h3.8L18 9.8 14.2 6zM20.7 7.1a1 1 0 0 0 0-1.4l-2.4-2.4a1 1 0 0 0-1.4 0L15 5.2 18.8 9z"/></svg>About</div>
<div class="abs bubble nav-bubble" style="left:242px;top:263px">
  <svg viewBox="0 0 24 24" fill="#222"><path d="M4 7h3l2-3h6l2 3h3a1 1 0 0 1 1 1v11a1 1 0 0 1-1 1H4a1 1 0 0 1-1-1V8a1 1 0 0 1 1-1zm8 3a4 4 0 1 0 0 8 4 4 0 0 0 0-8zm0 2a2 2 0 1 1 0 4 2 2 0 0 1 0-4z"/></svg>Gallery</div>
<div class="abs bubble nav-bubble" style="left:358px;top:263px">
  <svg viewBox="0 0 24 24" fill="#222"><path d="M12 21 3.5 12.5A5 5 0 0 1 12 5.5a5 5 0 0 1 8.5 7z"/></svg>Attraction</div>
<div class="abs bubble nav-bubble" style="left:458px;top:210px">
  <svg viewBox="0 0 24 24" fill="none" stroke="#222" stroke-width="3"><path d="M8 8a4 4 0 1 1 6 3.5c-1.5.8-2 1.5-2 3"/><circle cx="12" cy="19.5" r="1" fill="#222"/></svg>Enquiry</div>
<div class="abs bubble nav-bubble" style="left:493px;top:110px">
  <svg viewBox="0 0 24 24" fill="#222"><path d="M3 6h18v2l-9 5-9-5zM3 10l9 5 9-5v8H3z"/></svg>Contact</div>

<!-- welcome -->
<h2 class="abs section-title" style="left:56px;top:379px">
  <span class="title-icon"><svg viewBox="0 0 24 24" fill="#222"><path d="M12 3 2 12h3v8h5v-6h4v6h5v-8h3z"/></svg></span>
  <span><span class="accent">Welcome to</span> SANDBAR VILLA</span>
</h2>
<div class="abs welcome-copy" style="left:52px;top:419px;width:258px">
  <p>Lorem Ipsum is simply dummy text of the printing and typesetting industry. Lorem Ipsum has been the industry's standard dummy text ever since the 1500s, when an unknown printer took a galley to make a type specimen book. It has survived not only five centuries.</p>
  <p>Lorem Ipsum is simply dummy text of the printing and typesetting industry. Lorem Ipsum has been the industry's standard dummy text ever since the 1500s, when an unknown printer took a galley of type and scrambled.</p>
  <p>Lorem Ipsum is simply dummy text of the printing and typesetting industry. Lorem Ipsum has been the industry's standard dummy text ever since the 1500s, when an unknown printer took a galley of type and scrambled.</p>
</div>
<div class="abs col-divider"></div>

<!-- facilities -->
<h2 class="abs section-title" style="left:362px;top:379px">
  <span class="title-icon"><svg viewBox="0 0 24 24" fill="#222"><path d="M6 2h12v20H6zm2 3v2h3V5zm5 0v2h3V5zM8 9v2h3V9zm5 0v2h3V9zm-5 4v2h3v-2zm5 0v2h3v-2zm-3 4v5h4v-5z"/></svg></span>
  <span><span class="accent">Villa</span> Facilities</span>
</h2>
<div class="abs facility" style="top:412px">
  <div class="facility-photo" role="img" aria-label="Ocean front bedroom" style="background:linear-gradient(135deg,#7a6a5c,#d9d3cb 50%,#5f6d78)"></div>
  <h3>Ocean Front Rooms</h3>
  <p>Lorem Ipsum is simply dummy text of the printing and typesetting industry. Lorem...</p>
  <a href="#">Read More</a>
</div>
<div class="abs facility" style="top:487px">
  <div class="facility-photo" role="img" aria-label="Villa swimming pool" style="background:linear-gradient(135deg,#4f8f8c,#2e6a70 60%,#8bb5aa)"></div>
  <h3>Ocean Front Rooms</h3>
  <p>Lorem Ipsum is simply dummy text of the printing and typesetting industry. Lorem...</p>
  <a href="#">Read More</a>
</div>
<div class="abs facility" style="top:559px">
  <div class="facility-photo" role="img" aria-label="Evening dining area" style="background:linear-gradient(135deg,#3a2418,#c98a3a 50%,#2a2a4a)"></div>
  <h3>Ocean Front Rooms</h3>
  <p>Lorem Ipsum is simply dummy text of the printing and typesetting industry. Lorem...</p>
  <a href="#">Read More</a>
</div>

<!-- attractions -->
<div class="abs attractions" role="img" aria-label="Blue sea and sky backdrop"></div>
<h2 class="abs band-title" style="left:242px;top:673px">
  <span class="band-title-icon"><svg viewBox="0 0 24 24" fill="#fff"><path d="M12 2a7 7 0 0 0-7 7c0 5 7 13 7 13s7-8 7-13a7 7 0 0 0-7-7zm0 9.5A2.5 2.5 0 1 1 12 6.5a2.5 2.5 0 0 1 0 5z"/></svg></span>
  <span>Thailand <span class="dark">Attraction</span></span>
</h2>
<div class="abs card" style="left:44px">
  <div class="card-photo" role="img" aria-label="Turquoise lagoon between limestone cliffs" style="background:linear-gradient(180deg,#bfe3f2,#5f9a5a 45%,#6fd3d8 70%,#a8eef0)"></div>
  <div class="card-label">Popular Place</div>
</div>
<div class="abs card" style="left:198px">
  <div class="card-photo" role="img" aria-label="Crowded island beach with rock formations" style="background:linear-gradient(180deg,#d6e6ee,#4f6e4a 45%,#b9a98c 75%,#c7b9a0)"></div>
  <div class="card-label">Thailand Special</div>
</div>
<div class="abs card" style="left:350px">
  <div class="card-photo" role="img" aria-label="Lounge chair on beach facing water bungalows" style="background:linear-gradient(180deg,#8fbde0,#f2f5f7 30%,#5fc7d6 55%,#e8ddc8)"></div>
  <div class="card-label">Prestigious Linda</div>
</div>
<div class="abs card" style="left:502px">
  <div class="card-photo" role="img" aria-label="Traditional pavilion beside a garden pond" style="background:linear-gradient(180deg,#cfe0ea,#5e7a3a 40%,#8a3a2a 55%,#7f9a4a 80%)"></div>
  <div class="card-label">Prestigious Linda</div>
</div>

<!-- rates -->
<div class="abs rates" role="img" aria-label="Green tropical cliffs and longtail boats backdrop"></div>
<div class="abs bubble" style="left:331px;top:904px;width:26px;height:26px;background:transparent;border:1.5px solid #fff;box-shadow:none">
  <svg viewBox="0 0 24 24" width="14" height="14" fill="none" stroke="#fff" stroke-width="2"><rect x="3" y="5" width="18" height="16"/><path d="M3 10h18M8 3v4M16 3v4M7 13h2M11 13h2M15 13h2M7 17h2M11 17h2M15 17h2"/></svg>
</div>
<div class="abs rates-rule" style="left:228px"></div>
<div class="abs rates-rule" style="left:400px"></div>
<h2 class="abs rates-title" style="font-weight:400">Seasonal <span class="dark">Rates</span></h2>
<table class="abs rate-table">
  <colgroup><col style="width:146px"><col style="width:90px"><col style="width:91px"><col style="width:91px"><col style="width:91px"><col style="width:90px"></colgroup>
  <tr><th>Seasonal rates</th><th>max. occ.</th><th>Christmas</th><th>Winter</th><th>Summer</th><th>normal</th></tr>
  <tr><td>standard</td><td>2</td><td>$140</td><td>$120</td><td>$110</td><td>$100</td></tr>
  <tr><td>Superior</td><td>2</td><td>$180</td><td>$160</td><td>$150</td><td>$140</td></tr>
  <tr><td>Delux</td><td>2+1</td><td>$240</td><td>$220</td><td>$200</td><td>$190</td></tr>
</table>
<a class="abs book-btn" href="#">Book Now</a>

<!-- footer -->
<nav class="abs footer-nav">
  <span class="is-active">Home</span><span>About</span><span>Gallery</span><span>Attraction</span><span>Enquiry</span><span>Contact</span>
</nav>
<div class="abs footer-sand" role="img" aria-label="Sandy beach with seashells and starfish"></div>
<p class="abs copyright">© <b>SANDBAR VILLA</b> - 2015. All Rights Reserved.</p>

</body>
</html>
```